High Tech Software Startup needs Letterhead Design

We need a letterhead for a startup company base in Brazil. The letterhead should combine with our logo attached here.
We are a team of professionals in Java for web and mobile with iOS and android development.
We are looking for a modern and futuristc design.

Target Market(s)

CIO, IT managers of mid to big size companies

Industry/Entity Type

It Company

```html
<!DOCTYPE html>
<html lang="pt-BR">
<head>
<meta charset="utf-8">
<title>VOLTIQ Letterhead</title>
<link rel="stylesheet" href="https://fonts.googleapis.com/css2?family=Source+Sans+3:wght@400;700&family=Dancing+Script&display=swap">
<style>
  :root {
    --canvas: #ececec;
    --paper: #ffffff;
    --navy: #0b2d5c;
    --cyan: #00aeef;
    --deep: #26285e;
    --ink: #2e2e2e;
    --rule: #1a9ad6;
    --wash: #f1f2f4;
  }
  * { box-sizing: border-box; margin: 0; padding: 0; }
  html, body { width: 1200px; height: 1024px; overflow: hidden; }
  body {
    background: var(--canvas);
    font-family: "Source Sans 3", "Myriad Pro", sans-serif;
    color: var(--ink);
    position: relative;
  }
  .letterhead {
    position: absolute;
    left: 40px; top: 115px;
    width: 1120px; height: 793px;
    background:
      linear-gradient(160deg, transparent 38%, var(--wash) 39%, #fafafb 70%, transparent 71%),
      var(--paper);
    box-shadow: 0 6px 14px rgba(0,0,0,0.25);
    overflow: hidden;
  }
  .brand {
    position: absolute; left: 53px; top: 73px;
    display: flex; align-items: center; gap: 22px;
  }
  .brand-square {
    width: 92px; height: 92px;
    background: var(--navy);
    border-radius: 6px;
  }
  .brand-name {
    font-weight: 700; font-size: 84px; line-height: 1;
    color: var(--navy); letter-spacing: 1px;
  }
  .divider {
    position: absolute; left: 716px; top: 73px;
    width: 2px; height: 76px;
    background: linear-gradient(to bottom, transparent, var(--rule), transparent);
  }
  .contact {
    position: absolute; left: 892px; top: 84px;
    list-style: none; font-size: 15px; line-height: 16.5px; color: var(--ink);
  }
  .contact li { display: flex; align-items: center; gap: 3px; }
  .contact svg { width: 10px; height: 10px; fill: var(--rule); }
  .salutation {
    position: absolute; left: 53px; top: 199px;
    font-size: 18px;
  }
  .letter-body {
    position: absolute; left: 50px; top: 267px; width: 1030px;
    font-size: 15.5px; line-height: 19px;
  }
  .letter-body p + p { margin-top: 15px; }
  .signature {
    position: absolute; left: 50px; top: 651px;
  }
  .signature-name {
    font-family: "Dancing Script", cursive; font-size: 25px; color: #444;
  }
  .signature-role { font-size: 15px; margin-top: 2px; }
  .footer-band {
    position: absolute; left: 0; bottom: 0; width: 100%; height: 49px;
    background: linear-gradient(to right, var(--cyan), #0a6fa8 55%, var(--deep));
    display: flex; align-items: center; justify-content: center;
    color: #ffffff; font-size: 15.5px;
  }
</style>
</head>
<body>
  <article class="letterhead">
    <header>
      <div class="brand">
        <span class="brand-square"></span>
        <span class="brand-name">VOLTIQ</span>
      </div>
      <span class="divider"></span>
      <ul class="contact">
        <li><svg viewBox="0 0 10 10"><path d="M2 0.5l2 2-1 1.2c.6 1.3 1.6 2.3 2.9 2.9l1.2-1 2 2-1.2 1.6C4 9 1 6 .5 1.7z"/></svg>(11) 4000-2150</li>
        <li><svg viewBox="0 0 10 10"><path d="M0 2h10v6H0zM0 2l5 3.5L10 2" stroke="#fff" stroke-width=".8"/></svg>contato@voltiq.com.br</li>
        <li><svg viewBox="0 0 10 10"><circle cx="5" cy="5" r="5"/></svg>www.voltiq.com.br</li>
      </ul>
    </header>

    <p class="salutation">Lorem Ipsum,</p>

    <section class="letter-body">
      <p>Duis sit amet dolor sit amet dolor tempor iaculis ac nec ante. Proin nunc diam, egestas eu semper a, fermentum ac leo. Fusce sit amet tempor elit. Mauris auctor interdum massa vitae cursus. Ut adipiscing pellentesque nunc, eget tincidunt magna imperdiet non. Curabitur eleifend elementum nisl eget iaculis. Suspendisse scelerisque ligula a nunc faucibus sit amet elementum dolor dictum.</p>
      <p>Praesent condimentum,mi at ultrices fermentum, ipsum lectus consequat mauris, ut vulputate nibherat id eros. Vivamus ornare mattis libero at dictum. Praesent sodales metus sed nulla laoreet mollis. Curabitur non turpis in orci dignissim gravida. Aliquam tristique mauris a nibh vestibulum sagittis.</p>
      <p>Duis porta semper nibh, tincidunt aliquam metus euismod eget. Morbi varius varius pellentesque. Donec aliquam vulputate tortor non hendrerit. Suspendisse at ipsum ante, interdum porttitor ligula. Curabitur eu molestie sapien. Sed magna purus, faucibus quis pulvinar nec, commodo vel justo. Nam faucibus ornare varius. Vivamus sit amet felis vitae justo scelerisque malesuada. Etiam venenatis vehicula magna, aceleifend lorem ornare nec. Maecenas eu nisl vel nunc aliquet malesuada vel in lacus.</p>
      <p>Morbi et odio eu ante pharetra iaculis vitae eget arcu. Maecenas gravida, dui vel ultricies aliquet, dui arcu luctus ante, non dignissim ipsum tortor vel orci. um fringilla mi. Mauris porta feugiat nibh et fermentum. Donec scelerisque consequat lacinia.</p>
      <p>Curabitur ac diam ut quam ultrices laoreet at ut tellus. Maecenas vitae urna in lorem condimentum sollicitudin eget vel lacus. Ut nisi turpis, tristique ullamcorper laoreet nec, gravida nec est. Donec elementum malesuada volutpat. In ac arcu quis augue vehicula fringilla.</p>
      <p>Pellentesque habitant morbi tristique senectus et netus et malesuada fames ac turpis egestas.&nbsp; In posuere felis nec tortor. Pellentesque faucibus. Ut accumsan ultricies elit. Maecenas at justo id velit placerat molestie.</p>
    </section>

    <div class="signature">
      <p class="signature-name">Yours Name</p>
      <p class="signature-role">Company Director</p>
    </div>

    <footer class="footer-band">Rua das Palmeiras, 418 - 9º andar Cj. 902 CP 210 São Paulo - SP - Brasil CEP 01234-000</footer>
  </article>
</body>
</html>
```